TALL WAVE

I am in this industry for last 15 years we have done lots of commercial site like we work with ORBEL costruction, loam properties, DRV, quill construction.
We do all domestic and commercial wall and floor tiling, swimming pools, spas, paving, marbles blue stones and muchmore.

Specializing in the wall and floor Tiling, Waterproofing and floor preparations

Industry/Entity Type

Industry

Number of Pages Required

1 page

Font styles to use
Serif
Decorative

Colors

Designer to choose colors to be used in the design.

Requirements
Must have
• domestic and commercial indoor tiling, bathroom tiling and paving pictures
Nice to have
• beautiful bathroom pictures with tile

```html
<!DOCTYPE html>
<html lang="en">
<head>
<meta charset="utf-8">
<title>Tall Wave — Wall &amp; Floor Tiling</title>
<link href="https://fonts.googleapis.com/css2?family=Open+Sans:wght@300;400;600;700;800&display=swap" rel="stylesheet">
<style>
  :root {
    --brand-blue: #1e8fd6;
    --panel-blue: rgba(30, 136, 210, 0.78);
    --about-tint: rgba(24, 120, 200, 0.55);
    --contact-tint: rgba(14, 150, 215, 0.82);
    --send-green: #19c7a2;
    --ink: #333a40;
    --muted: #8a9096;
    --white: #ffffff;
    --field-border: #c9d7e2;
  }
  * { box-sizing: border-box; margin: 0; padding: 0; }
  html, body { width: 686px; height: 1200px; overflow: hidden; background: var(--white); }
  body { font-family: "Open Sans", Arial, sans-serif; color: var(--ink); position: relative; }

  /* header */
  .site-header { position: absolute; top: 0; left: 0; width: 686px; height: 45px; background: var(--white); display: flex; align-items: center; justify-content: space-between; padding: 0 28px 0 98px; }
  .brand { font-weight: 400; font-size: 17px; color: var(--ink); letter-spacing: 0.2px; display: flex; align-items: center; gap: 7px; }
  .brand-mark { width: 9px; height: 9px; border-radius: 50%; background: var(--ink); }
  .main-nav { display: flex; gap: 42px; font-size: 8px; font-weight: 700; letter-spacing: 0.6px; color: #444; }
  .main-nav .is-active { color: var(--brand-blue); }

  /* hero */
  .hero { position: absolute; top: 45px; left: 0; width: 686px; height: 345px; overflow: hidden; }
  .hero-photo { position: absolute; inset: 0; background: linear-gradient(120deg, #5a5248 0%, #c9b9a2 30%, #e9e1d2 55%, #d7c6ab 75%, #7d6c55 100%); }
  .hero-panel { position: absolute; left: 96px; top: 51px; width: 377px; height: 259px; background: var(--panel-blue); padding: 20px 22px; color: var(--white); }
  .hero-kicker { font-size: 10px; font-weight: 700; letter-spacing: 1.4px; }
  .hero-title { font-size: 38px; font-weight: 300; line-height: 1.1; margin-top: 4px; }
  .hero-tagline { font-size: 8px; font-weight: 600; margin-top: 3px; }
  .hero-text { font-size: 8.5px; line-height: 1.7; margin-top: 34px; opacity: 0.95; }
  .slider-dots { position: absolute; left: 322px; top: 312px; display: flex; gap: 6px; }
  .slider-dots span { width: 7px; height: 7px; border-radius: 50%; background: rgba(255,255,255,0.6); }
  .slider-dots span.is-current { background: var(--brand-blue); }

  /* about */
  .about { position: absolute; top: 390px; left: 0; width: 686px; height: 388px; overflow: hidden; }
  .about-photo { position: absolute; inset: 0; background: linear-gradient(100deg, #27343d 0%, #4b5a63 35%, #8d9aa2 60%, #d9dfe2 78%, #6d7a83 100%); }
  .about-tint { position: absolute; inset: 0; background: var(--about-tint); }
  .about-content { position: absolute; top: 140px; left: 0; width: 686px; text-align: center; color: var(--white); }
  .about-title { font-size: 34px; font-weight: 300; }
  .about-text { width: 400px; margin: 6px auto 0; font-size: 8.5px; line-height: 1.7; }

  /* contact */
  .contact { position: absolute; top: 778px; left: 0; width: 686px; height: 365px; overflow: hidden; }
  .contact-photo { position: absolute; inset: 0; background: linear-gradient(135deg, #1f4d5c 0%, #3f8a96 40%, #7bb7bf 70%, #2e5f6b 100%); }
  .contact-tint { position: absolute; inset: 0; background: var(--contact-tint); }
  .contact-title { position: absolute; left: 98px; top: 56px; font-size: 19px; font-weight: 400; color: var(--white); }
  .contact-rule { position: absolute; left: 98px; top: 92px; width: 40px; height: 1px; background: rgba(255,255,255,0.7); }
  .contact-info { position: absolute; left: 98px; top: 124px; width: 180px; color: var(--white); font-size: 7.5px; line-height: 1.6; }
  .contact-info h3 { font-size: 9px; font-weight: 400; margin-bottom: 16px; }
  .info-row { display: flex; gap: 6px; align-items: flex-start; margin-bottom: 8px; }
  .info-row svg { flex: none; margin-top: 1px; }
  .socials { display: flex; gap: 8px; margin-top: 4px; }
  .socials span { width: 10px; height: 10px; border-radius: 50%; background: var(--white); }

  .contact-form { position: absolute; left: 293px; top: 139px; width: 292px; }
  .field-row { display: flex; gap: 4px; margin-bottom: 4px; }
  .field { flex: 1; height: 19px; background: var(--white); border: 1px solid var(--field-border); font-size: 6.5px; color: var(--muted); padding: 5px 6px; }
  .field-message { height: 82px; margin-bottom: 8px; }
  .send-button { width: 118px; height: 22px; background: var(--send-green); color: var(--white); font-size: 7.5px; font-weight: 700; letter-spacing: 1px; display: flex; align-items: center; justify-content: center; gap: 8px; }

  /* footer */
  .site-footer { position: absolute; top: 1143px; left: 0; width: 686px; height: 57px; background: var(--white); display: flex; align-items: center; justify-content: space-between; padding: 0 40px 0 98px; font-size: 6.5px; color: var(--muted); letter-spacing: 0.3px; }
  .footer-links { display: flex; gap: 24px; }
</style>
</head>
<body>

<header class="site-header">
  <div class="brand"><span class="brand-mark"></span>Tall Wave</div>
  <nav class="main-nav">
    <span class="is-active">PRODUCTS</span>
    <span>ABOUT</span>
    <span>CONTACT</span>
  </nav>
</header>

<section class="hero">
  <div class="hero-photo" role="img" aria-label="Bright tiled bathroom with marble vanity, mosaic wall and flowers"></div>
  <div class="hero-panel">
    <p class="hero-kicker">LOREM IPSUM DOLOR SIT AMET</p>
    <h1 class="hero-title">lorem ipsum</h1>
    <p class="hero-tagline">Tiles laid with care, built to last</p>
    <p class="hero-text">We lay domestic and commercial wall and floor tiles, pools, spas, paving and bluestone. Every job gets careful floor preparation and full waterproofing so your rooms look sharp and stay dry for years to come.</p>
  </div>
  <div class="slider-dots"><span></span><span class="is-current"></span><span></span><span></span></div>
</section>

<section class="about">
  <div class="about-photo" role="img" aria-label="Modern bathroom with freestanding tub, glass shower and mosaic tiled wall"></div>
  <div class="about-tint"></div>
  <div class="about-content">
    <h2 class="about-title">about</h2>
    <p class="about-text">For fifteen years we have tiled homes, offices and commercial sites across the region. From bathrooms and kitchens to pools and outdoor paving, our team handles waterproofing, floor preparation and precise finishing on every project we take on.</p>
  </div>
</section>

<section class="contact">
  <div class="contact-photo" role="img" aria-label="Stone tiled bathroom with basin and textured feature wall"></div>
  <div class="contact-tint"></div>
  <h2 class="contact-title">Contact Us</h2>
  <div class="contact-rule"></div>

  <div class="contact-info">
    <h3>Contact Information</h3>
    <div class="info-row">
      <svg width="8" height="10" viewBox="0 0 8 10"><path d="M4 0C1.8 0 0 1.7 0 3.9 0 6.8 4 10 4 10s4-3.2 4-6.1C8 1.7 6.2 0 4 0zm0 5.3a1.4 1.4 0 1 1 0-2.8 1.4 1.4 0 0 1 0 2.8z" fill="#fff"/></svg>
      <div><strong>Tall Wave</strong><br>12 Harbour Lane<br>Southbank VIC 3006</div>
    </div>
    <div class="info-row">
      <svg width="8" height="8" viewBox="0 0 8 8"><path d="M1.6 0.3l1.2 1.6-.7 1.1c.5 1 1.3 1.8 2.3 2.3l1.1-.7 1.6 1.2-.6 1.6C3.6 7.3.7 4.4.3 1.4z" fill="#fff"/></svg>
      <div>(03) 5550 1842</div>
    </div>
    <div class="info-row">
      <svg width="9" height="7" viewBox="0 0 9 7"><rect x="0.5" y="0.5" width="8" height="6" fill="none" stroke="#fff"/><path d="M0.5 0.5l4 3.2 4-3.2" fill="none" stroke="#fff"/></svg>
      <div>hello@tallwave.com</div>
    </div>
    <div class="socials"><span></span><span></span></div>
  </div>

  <form class="contact-form">
    <div class="field-row">
      <div class="field">Your Name</div>
      <div class="field">Phone Number</div>
    </div>
    <div class="field-row">
      <div class="field">Email Address</div>
      <div class="field">Company</div>
    </div>
    <div class="field field-message">Message</div>
    <div class="send-button">SEND
      <svg width="8" height="6" viewBox="0 0 8 6"><path d="M0 3h7M4.5 0.5L7 3 4.5 5.5" fill="none" stroke="#fff" stroke-width="1"/></svg>
    </div>
  </form>
</section>

<footer class="site-footer">
  <span>© Copyright 2017 Tall Wave. All rights reserved.</span>
  <div class="footer-links"><span>Privacy Policy</span><span>Terms of Use</span></div>
</footer>

</body>
</html>
```